Lawn sign for construction company

Would like this to be a very clean and high end design for luxury homes. We need a yard sign designed that includes the company logo, website, phone number and major service offerings (residential and commercial renovations and maintenance)
The company website is brackwellbuilders.com all other contact info is in the attachments
Target Market(s)
Luxury home owners and business owners
Industry/Entity Type
Construction/Home Improvement
Font styles to use
Other font styles liked:
- See company logo and other graphics included for title text fonts. All other fonts can be standard sans serif.
Colors
0054AA
0677BA
7BADD7
CADEEF
E8F1F8
Requirements
Must have
- Clean, easy to read design, would like 2 sided sign. A main sign side and back side which states “free estimates, and includes the website and phone number. Must also match the color scheme of the provided logo and other company images. Dark Navy blue primary color, gray secondary color, and orange as an accent color.
Nice to have
- 2nd sign side very simple design
Should not have
- Too many graphics limit to 1-3 colors

```html
<!DOCTYPE html>
<html lang="en">
<head>
<meta charset="utf-8">
<title>Brackwell Construction Company – Lawn Sign</title>
<link href="https://fonts.googleapis.com/css2?family=Montserrat:wght@400;500;600;700;800&display=swap" rel="stylesheet">
<style>
  :root {
    --stage: #767474;
    --sign-edge: #d6d6d6;
    --panel-grey: #c9c9c9;
    --panel-light: #dcdcdc;
    --navy: #03085a;
    --orange: #e8730a;
    --white: #ffffff;
  }
  html, body {
    margin: 0;
    padding: 0;
    width: 1200px;
    height: 1200px;
    overflow: hidden;
    background: var(--stage);
    font-family: "Montserrat", Arial, sans-serif;
  }
  .sign {
    position: absolute;
    left: 225px;
    width: 750px;
    height: 500px;
    display: block;
  }
  .sign--front { top: 72px; }
  .sign--back { top: 627px; }
  .sign-edge { fill: var(--sign-edge); }
  .panel { fill: var(--panel-grey); stroke: var(--navy); stroke-width: 1.5; }
  .panel-light { fill: var(--panel-light); }
  .navy-band { fill: var(--navy); }
  .orange-chevron { fill: var(--orange); }
  .company-name {
    fill: var(--orange);
    font-weight: 800;
    font-size: 34px;
    letter-spacing: 1px;
  }
  .headline {
    fill: var(--white);
    font-weight: 700;
    font-size: 30px;
    letter-spacing: 2.5px;
  }
  .phone-large {
    fill: var(--white);
    font-weight: 700;
    font-size: 74px;
    letter-spacing: -1px;
  }
  .website {
    fill: var(--orange);
    font-weight: 700;
    font-size: 27px;
    letter-spacing: 3.5px;
  }
  .contact-label {
    fill: var(--white);
    font-weight: 400;
    font-size: 23px;
    letter-spacing: 1.5px;
  }
  .phone-dotted {
    fill: var(--white);
    font-weight: 600;
    font-size: 62px;
    letter-spacing: 2px;
  }
  .divider { stroke: var(--orange); stroke-width: 2; }
  .services {
    fill: var(--white);
    font-weight: 500;
    font-size: 21.5px;
    letter-spacing: 0.6px;
  }
  .bullet { fill: var(--orange); }
  .phone-icon { fill: var(--orange); }
  .phone-waves { fill: none; stroke: var(--orange); stroke-width: 2.6; stroke-linecap: round; }
</style>
</head>
<body>

<!-- Front side -->
<svg class="sign sign--front" viewBox="0 0 750 500" aria-label="Front side of lawn sign">
  <rect class="sign-edge" x="0" y="0" width="750" height="500"/>
  <rect class="panel" x="17" y="14" width="718" height="473"/>
  <polygon class="panel-light" points="735,20 735,233 376,335 300,300"/>
  <polygon class="navy-band" points="17,233 376,335 735,233 735,487 17,487"/>
  <polygon class="orange-chevron" points="40,240 376,318 712,240 376,335"/>

  <text class="company-name" x="375" y="155" text-anchor="middle">BRACKWELL</text>
  <text class="company-name" x="375" y="195" text-anchor="middle">CONSTRUCTION COMPANY</text>

  <text class="headline" x="375" y="371" text-anchor="middle">CALL FOR FREE ESTIMATES</text>

  <g class="phone-glyph" transform="translate(80,395)">
    <path class="phone-icon" d="M8 2c3-2 6-1 7 1l5 9c1 2 0 4-2 5l-3 2c2 6 7 11 13 14l2-3c1-2 3-3 5-2l9 4c2 1 3 4 1 7l-3 4c-2 2-5 3-8 2C20 41 5 26 1 12 0 8 3 4 8 2z"/>
    <path class="phone-waves" d="M25 6a16 16 0 0 1 14 14"/>
    <path class="phone-waves" d="M26 -2a24 24 0 0 1 21 21"/>
    <path class="phone-waves" d="M24 13a8 8 0 0 1 7 7"/>
  </g>
  <text class="phone-large" x="408" y="440" text-anchor="middle">800-555-0199</text>

  <text class="website" x="375" y="474" text-anchor="middle">www.brackwellbuilders.com</text>
</svg>

<!-- Back side -->
<svg class="sign sign--back" viewBox="0 0 750 500" aria-label="Back side of lawn sign">
  <rect class="sign-edge" x="0" y="0" width="750" height="500"/>
  <rect class="panel" x="19" y="16" width="716" height="470"/>
  <polygon class="panel-light" points="735,20 735,233 376,335 300,300"/>
  <polygon class="navy-band" points="19,233 376,335 735,233 735,486 19,486"/>
  <polygon class="orange-chevron" points="40,240 376,318 712,240 376,335"/>

  <text class="company-name" x="375" y="155" text-anchor="middle">BRACKWELL</text>
  <text class="company-name" x="375" y="195" text-anchor="middle">CONSTRUCTION COMPANY</text>

  <text class="contact-label" x="375" y="360" text-anchor="middle">CONTACT US ON</text>
  <text class="phone-dotted" x="375" y="412" text-anchor="middle">800.555.0199</text>
  <line class="divider" x1="103" y1="423" x2="646" y2="423"/>

  <text class="services" x="375" y="449" text-anchor="middle">RESIDENTIAL RENOVATIONS <tspan class="bullet">■</tspan> COMMERCIAL</text>
  <text class="services" x="375" y="472" text-anchor="middle">RENOVATIONS <tspan class="bullet">■</tspan> MAINTENANCE</text>
</svg>

</body>
</html>
```